Laser Engraving Business Needs Shopify Front and Backend Site Design

We are starting up a brick laser engraving business and need the Shopify front and back end created. The design will stylistically match the logo we had designed and is attached (specifically the embossed shadowed logo). The ideal design will be dark themed.

The back end will support a standard product template with the ability to group products by type. The design will also include the ability to track visitor interaction with the site, as well as links to the companies social media accounts. Billing will be handled through Shopify and linked to company accounts.
Updates

Project has been guaranteed and 2nd place money added. Project requirements were adjusted slightly to reflect feedback that was sent out. Great submissions so far!

Industry/Entity Type

Business

Font styles to use
Sans Serif

Colors
ec1f27

Requirements
Must have
• The design will stylistically match the logo we had designed and is attached and be dark overall.
• Front end must include an About Us, Products, Social Media, Custom Design.
• The back end will support modular products grouped by type.
Nice to have
• A Placeholder page supporting photos, video and blog type content.

```html
<!DOCTYPE html>
<html lang="en">
<head>
<meta charset="utf-8">
<title>Brickmark – Brick Wall Laser Engraving</title>
<link rel="stylesheet" href="https://fonts.googleapis.com/css2?family=Montserrat:wght@400;500;600;700&family=Arimo:ital,wght@0,400;0,700;1,400&display=swap">
<style>
  :root {
    --brand-red: #ec1f27;
    --nav-dark: #3a3a3a;
    --nav-active: #f0737a;
    --ink: #111111;
    --muted: #7a7a7a;
    --white: #ffffff;
    --rule: #e4e4e4;
    --photo-light: #e3e5ea;
    --photo-mid: #c3c7ce;
    --photo-dark: #7f848d;
  }
  * { box-sizing: border-box; margin: 0; padding: 0; }
  html, body { width: 1200px; height: 558px; overflow: hidden; background: var(--white); }
  body { font-family: "Montserrat", sans-serif; position: relative; }

  .utility-bar { position: absolute; top: 0; left: 0; width: 1200px; height: 31px; background: var(--white); }
  .menu-toggle { position: absolute; left: 240px; top: 11px; width: 10px; }
  .contact-item { position: absolute; top: 10px; font-family: "Arimo", sans-serif; font-size: 9.5px; color: var(--ink); display: flex; align-items: center; gap: 6px; }
  .contact-item.phone { left: 695px; }
  .contact-item.hours { left: 768px; font-style: italic; }
  .search-box { position: absolute; left: 881px; top: 0; width: 90px; height: 31px; border-left: 1px solid var(--rule); border-right: 1px solid var(--rule); font-family: "Arimo", sans-serif; font-size: 9px; color: #b5b5b5; padding: 10px 0 0 11px; white-space: nowrap; overflow: hidden; }
  .search-box svg { position: absolute; right: 10px; top: 10px; }

  .main-nav { position: absolute; top: 31px; left: 0; width: 1200px; height: 62px; background: var(--nav-dark); }
  .brand-name { position: absolute; left: 232px; top: 21px; display: flex; align-items: center; gap: 7px; font-weight: 700; font-size: 17px; letter-spacing: 0.5px; color: var(--brand-red); text-transform: uppercase; line-height: 20px; }
  .brand-mark { width: 17px; height: 17px; background: var(--brand-red); }
  .nav-links { position: absolute; right: 244px; top: 25px; display: flex; gap: 19px; list-style: none; }
  .nav-links li { font-size: 10.8px; font-weight: 600; letter-spacing: 0.6px; color: var(--white); }
  .nav-links li.active { color: var(--nav-active); }

  .hero { position: absolute; top: 93px; left: 0; width: 1200px; height: 406px; }
  .hero-photo { position: absolute; inset: 0; background: linear-gradient(90deg, var(--photo-dark) 0%, #b9bcc3 7%, var(--photo-light) 14%, var(--photo-light) 32%, #d6d8dd 50%, var(--photo-light) 75%, var(--photo-mid) 100%); }
  .hero-photo::after { content: ""; position: absolute; left: 0; right: 0; bottom: 0; height: 130px; background: linear-gradient(180deg, rgba(90,94,102,0) 0%, rgba(90,94,102,0.4) 100%); }
  .hero-copy { position: absolute; left: 5px; width: 1200px; text-align: center; color: var(--ink); }
  .hero-kicker { top: 130px; font-size: 18px; font-weight: 600; letter-spacing: 0.5px; }
  .hero-title { top: 152px; font-size: 55px; font-weight: 700; letter-spacing: 4px; line-height: 58px; }
  .shop-button { position: absolute; left: 491px; top: 290px; width: 218px; height: 46px; background: var(--brand-red); color: var(--white); font-size: 14px; font-weight: 500; letter-spacing: 1.5px; display: flex; align-items: center; justify-content: center; }

  .service-band { position: absolute; top: 499px; left: 0; width: 1200px; height: 59px; background: var(--white); border-bottom: 1px solid var(--rule); }
  .service-item { position: absolute; top: 14px; display: flex; align-items: center; gap: 13px; font-family: "Arimo", sans-serif; font-size: 8px; line-height: 10px; text-transform: uppercase; }
  .service-item strong { display: block; color: #2b2b2b; }
  .service-item span { color: var(--muted); }
  .service-item.guarantee { left: 301px; }
  .service-item.shipping { left: 538px; }
  .service-item.support { left: 791px; }
</style>
</head>
<body>
  <header class="utility-bar">
    <svg class="menu-toggle" viewBox="0 0 10 8" width="10" height="8"><rect y="0" width="10" height="1.4" fill="#222"/><rect y="3.3" width="10" height="1.4" fill="#222"/><rect y="6.6" width="10" height="1.4" fill="#222"/></svg>
    <div class="contact-item phone">
      <svg width="10" height="10" viewBox="0 0 24 24"><path fill="#111" d="M6.6 10.8a15.1 15.1 0 0 0 6.6 6.6l2.2-2.2c.3-.3.7-.4 1-.2 1.1.4 2.3.6 3.6.6.6 0 1 .4 1 1V20c0 .6-.4 1-1 1A17 17 0 0 1 3 4c0-.6.4-1 1-1h3.5c.6 0 1 .4 1 1 0 1.3.2 2.5.6 3.6.1.3 0 .7-.2 1z"/></svg>
      555 0142
    </div>
    <div class="contact-item hours">
      <svg width="10" height="10" viewBox="0 0 24 24"><circle cx="12" cy="12" r="9.5" fill="none" stroke="#111" stroke-width="3"/><path d="M12 6v6h4" fill="none" stroke="#111" stroke-width="2.5"/></svg>
      Mon–Sat: 7:00–19:00
    </div>
    <div class="search-box">Search our s
      <svg width="10" height="10" viewBox="0 0 24 24"><circle cx="10" cy="10" r="7" fill="none" stroke="#111" stroke-width="3.5"/><path d="M15 15l7 7" stroke="#111" stroke-width="4"/></svg>
    </div>
  </header>

  <nav class="main-nav">
    <div class="brand-name"><span class="brand-mark"></span>Brickmark</div>
    <ul class="nav-links">
      <li class="active">HOME</li>
      <li>ABOUT US</li>
      <li>PRODUCTS</li>
      <li>NEWS</li>
      <li>BLOG</li>
      <li>CONTACT US</li>
    </ul>
  </nav>

  <section class="hero">
    <div class="hero-photo" role="img" aria-label="Bright studio interior with a white painted brick wall, two desks with lamps and stools, and a large window"></div>
    <p class="hero-copy hero-kicker">LASER ENGRAVING TECHNOLOGY</p>
    <h1 class="hero-copy hero-title">BRICK WALL<br>LASER ENGRAVING</h1>
    <div class="shop-button">SHOP NOW</div>
  </section>

  <section class="service-band">
    <div class="service-item guarantee">
      <svg width="20" height="20" viewBox="0 0 24 24"><circle cx="12" cy="12" r="10.5" fill="none" stroke="#222" stroke-width="1.8"/><text x="12" y="16.5" text-anchor="middle" font-family="Arimo, sans-serif" font-size="13" font-weight="700" fill="#222">$</text></svg>
      <div><strong>100% Money Back</strong><span>Guarantee</span></div>
    </div>
    <div class="service-item shipping">
      <svg width="20" height="16" viewBox="0 0 24 18"><path fill="#222" d="M5 2h14l3 6v7h-2.5a2.5 2.5 0 0 1-5 0h-5a2.5 2.5 0 0 1-5 0H2V8zm1.5 2L4.5 8h15l-2-4z"/></svg>
      <div><strong>Free Shipping</strong><span>On order over 500$</span></div>
    </div>
    <div class="service-item support">
      <svg width="18" height="18" viewBox="0 0 24 24"><path fill="#222" d="M6.6 10.8a15.1 15.1 0 0 0 6.6 6.6l2.2-2.2c.3-.3.7-.4 1-.2 1.1.4 2.3.6 3.6.6.6 0 1 .4 1 1V20c0 .6-.4 1-1 1A17 17 0 0 1 3 4c0-.6.4-1 1-1h3.5c.6 0 1 .4 1 1 0 1.3.2 2.5.6 3.6.1.3 0 .7-.2 1z"/></svg>
      <div><strong>24-Hour</strong><span>Active Support</span></div>
    </div>
  </section>
</body>
</html>
```